Bea's Logo and Cards

We are a mobile food cart business. We are looking for a logo similar to a "Mom" tattoo, with the inflated heart in red and a yellow ribbon going across heart in yellow, with the word "Bea's" on the ribbon in black. On the back of the card we want our venues done in bullet points: Catering, Birthday Parties, Concessions, Family Reunions, Corporate Functions, Festivals, School and Business Events.

Industry/Entity Type

Business

Contact Information for Business Card

Bea's Rolling Galley
4870 Larkspur Road
S. Alder Falls, OH 45871
317-519-2036
beasrollinggalley@quillbox.net

```html
<!DOCTYPE html>
<html lang="en">
<head>
<meta charset="utf-8">
<title>Bea's Rolling Galley – Business Cards</title>
<link rel="stylesheet" href="https://fonts.googleapis.com/css2?family=Alfa+Slab+One&family=Didact+Gothic&family=Montserrat:wght@700&display=swap">
<style>
  :root {
    --backdrop: #d8dfdb;
    --card: #ffffff;
    --ink: #111111;
    --heart-red: #e2261c;
    --card-shadow: rgba(60, 75, 70, 0.22);
  }
  * { box-sizing: border-box; margin: 0; padding: 0; }
  html, body { width: 1200px; height: 1000px; overflow: hidden; }
  body {
    position: relative;
    background: var(--backdrop);
    font-family: "Didact Gothic", sans-serif;
    color: var(--ink);
  }
  .card {
    position: absolute;
    background: var(--card);
    border-radius: 34px;
    box-shadow: 0 14px 30px var(--card-shadow);
  }
  .brand {
    display: flex;
    align-items: center;
    justify-content: center;
    gap: 12px;
  }
  .brand-dot {
    border-radius: 50%;
    background: var(--heart-red);
    flex: none;
  }
  .brand-name {
    font-family: "Alfa Slab One", serif;
    font-weight: 400;
    color: var(--ink);
    letter-spacing: 1px;
    white-space: nowrap;
  }

  /* Back of card: venues */
  .card-back {
    left: 600px; top: 80px; width: 540px; height: 320px;
    padding: 28px 30px;
    display: flex; flex-direction: column; align-items: center;
  }
  .card-back .brand-dot { width: 24px; height: 24px; }
  .card-back .brand-name { font-size: 16px; }
  .venue-list {
    list-style: none;
    margin-top: 16px;
    text-align: center;
    font-family: "Alfa Slab One", serif;
    font-size: 20px;
    line-height: 1.3;
    letter-spacing: 1.5px;
    text-transform: uppercase;
  }

  /* Front of card: contact */
  .card-front {
    left: 70px; top: 440px; width: 600px; height: 340px;
    padding: 60px 40px 0;
    display: flex; flex-direction: column; align-items: center;
  }
  .card-front .brand-dot { width: 64px; height: 64px; }
  .card-front .brand-name { font-size: 28px; }
  .contact {
    margin-top: 40px;
    font-style: normal;
    font-size: 18px;
    line-height: 1.35;
    text-align: left;
  }
  .contact .email {
    font-family: "Montserrat", sans-serif;
    font-weight: 700;
    font-size: 18px;
  }

  /* Standalone mark */
  .brand-standalone {
    position: absolute;
    left: 860px; top: 850px; width: 310px;
  }
  .brand-standalone .brand-dot { width: 44px; height: 44px; }
  .brand-standalone .brand-name { font-size: 20px; }
</style>
</head>
<body>
  <section class="card card-back" aria-label="Card back: venues">
    <div class="brand">
      <span class="brand-dot"></span>
      <span class="brand-name">Bea's Rolling Galley</span>
    </div>
    <ul class="venue-list">
      <li>Catering</li>
      <li>Birthday Parties</li>
      <li>Family Reunions</li>
      <li>Concessions</li>
      <li>Corporate Functions</li>
      <li>Festivals</li>
      <li>School and Business Events</li>
    </ul>
  </section>

  <section class="card card-front" aria-label="Card front: contact">
    <div class="brand">
      <span class="brand-dot"></span>
      <span class="brand-name">Bea's Rolling Galley</span>
    </div>
    <address class="contact">
      <div>4870 Larkspur Road S. Alder Falls, OH 45871</div>
      <div>317 - 519 - 2036</div>
      <div class="email">beasrollinggalley@quillbox.net</div>
    </address>
  </section>

  <div class="brand brand-standalone">
    <span class="brand-dot"></span>
    <span class="brand-name">Bea's Rolling Galley</span>
  </div>
</body>
</html>
```